Home Page Redesign for Pet Website

Looking to redesign the home page of our WORDPRESS website which will be renamed The Animal Cover Handbook 2015.

Looking for clean design which communicates clarity.
Updates

This is for a Wordpress site.

Please note that the design MUST include the content which is shown in the table in the brief!

Hi Thanks for the designs so far. We have just updated the brief to provide more information and clarify a few issues. We have also now included a couple of layout suggestions. They are just suggestions but it should give you a better idea of what we are looking for. And we have just increased the budget for 1st place by £120. Please feel free to message me if you have any questions. Many thanks. Mabel

Please note that the new brief is in a file dated 25 Jan!

Project Deadline Extended
Reason: We have extended the deadline so we can continue working with the designers who have submitted designs we like. If you have any new designs please submit them by the original deadline of 7.37pm this evening (GMT). We are planning to make our final decision by Friday this week.

Target Market(s)

UK pet owners. All ages but largest age group is 35-50.

Industry/Entity Type

Insurance

Requirements
Must have
• Three clear content groups - LEARN, RESEARCH, CAMPAIGN (see brief for more details).
Stock photos with dogs and cats
Use current colour scheme
Must work with existing inner pages.
Existing font.. but 1pt larger
See brief for more details
Should not have
• Logo
Content from Existing Page (except for footer content... and menu headings).

```html
<!DOCTYPE html>
<html lang="en">
<head>
<meta charset="utf-8">
<title>The Animal Cover Handbook 2015</title>
<link href="https://fonts.googleapis.com/css2?family=Open+Sans:wght@400;600;700&family=Arimo:wght@400;700&display=swap" rel="stylesheet">
<style>
:root{
  --orange:#f47a22;
  --orange-light:#ff9a3c;
  --orange-deep:#f25a12;
  --blue:#1f47d6;
  --blue-light:#3a78f0;
  --blue-text:#2456d6;
  --navy:#131a52;
  --navy-deep:#0d1236;
  --ink:#333;
  --muted:#555;
  --line:#d9d9d9;
  --panel-head:#efefef;
  --white:#fff;
}
*{margin:0;padding:0;box-sizing:border-box}
html,body{width:989px;height:1200px;overflow:hidden}
body{position:relative;background:var(--white);font-family:"Open Sans",sans-serif;color:var(--ink)}
.abs{position:absolute}
a{color:inherit;text-decoration:none}

/* header */
.site-name{left:131px;top:18px;width:160px;font-size:17px;line-height:19px;font-weight:600;color:var(--orange)}
.social-top{right:131px;top:16px;display:flex;gap:8px;font-size:9px;font-weight:600;color:var(--blue-text)}
.search{left:680px;top:38px;width:178px;height:24px;border:1px solid #ccc;border-radius:2px;font-size:8px;color:#555;padding:6px 9px;background:#fafafa}
.search svg{position:absolute;right:7px;top:5px}

.main-nav{left:0;top:71px;width:989px;height:34px;background:linear-gradient(#ff8c2f,var(--orange-deep));}
.main-nav ul{list-style:none;display:flex;margin-left:147px;height:34px}
.main-nav li{color:var(--white);font-size:12px;line-height:34px;padding:0 14px;border-right:1px solid rgba(255,255,255,.3)}
.main-nav li:last-child,.main-nav li:nth-last-child(2){border-right:0}
.main-nav li:first-child{padding-left:14px}

/* feature tiles */
.tile{top:145px;width:174px;height:155px;border-radius:10px 4px 16px 4px;color:var(--white);text-align:center;padding-top:14px}
.tile.blue{background:linear-gradient(160deg,var(--blue-light),var(--blue))}
.tile.blue.dark{background:linear-gradient(160deg,#2a60e6,#1638b8)}
.tile.orange{background:linear-gradient(160deg,var(--orange-light),var(--orange-deep))}
.tile .icon{height:62px;display:flex;justify-content:center;align-items:center}
.tile h3{font-weight:400;font-size:15.5px;line-height:17px;margin-top:4px}
.tile p{font-size:8px;line-height:13.5px;margin-top:4px;opacity:.9;padding:0 20px}

/* content groups */
.group{top:335px;height:296px;border:1px solid var(--line);border-radius:2px}
.group-head{height:50px;background:linear-gradient(#f7f7f7,#e9e9e9);border-bottom:1px solid var(--line);padding:10px 0 0 28px}
.group-head .kicker{font-size:11.5px;color:#222;line-height:14px}
.group-head h2{font-size:14px;font-weight:400;line-height:17px;color:var(--blue-text)}
.group-head h2.orange{color:var(--orange)}
.group ul{list-style:none}
.learn-list{padding:8px 0 0 28px}
.learn-list li{font-size:8.7px;line-height:13.5px;margin-bottom:9.6px;width:190px}
.research-body{padding:8px 0 0 29px;font-size:8.7px}
.research-body h4{font-size:8.7px;font-weight:600;margin-bottom:7px}
.research-cols{display:flex}
.research-cols ul{width:96px}
.research-cols li{line-height:16.8px}
.research-cols ul+ul{margin-top:4px}
.research-body p{line-height:13.5px;margin-top:7px;width:200px}
.campaign-list{padding:14px 0 0 22px}
.campaign-list li{font-size:8.7px;line-height:13.5px;margin-bottom:9.7px}

/* articles */
.section-title{left:135px;top:679px;font-size:18px;font-weight:400;color:#222}
.photo{border-radius:2px}
.article{width:180px}
.article h3{font-size:11px;line-height:14px;font-weight:400;color:var(--orange)}
.article p{font-size:8.2px;line-height:13.6px;color:var(--muted);margin-top:2px}
.article .more{display:block;font-size:8.3px;font-weight:600;color:#333;margin-top:5px}

/* footer */
.footer{left:0;top:881px;width:989px;height:270px;background:var(--navy)}
.footer-bottom{left:0;top:1151px;width:989px;height:49px;background:var(--navy-deep);color:#ddd;font-size:9px;padding:17px 0 0 131px}
.widget{top:910px;width:171px;height:214px;background:var(--white);border-radius:3px;overflow:hidden;font-family:"Arimo",sans-serif}
.widget-head{height:24px;padding:5px 0 0 14px;font-family:"Open Sans",sans-serif;font-size:11px;font-weight:600;color:#10205a}
.widget.fb .widget-head{background:#dde6f3}
.widget.tw .widget-head{background:#55c4de}
.fb-page{display:flex;gap:6px;padding:5px 6px;height:32px;font-size:7.5px}
.avatar{width:26px;height:26px;background:#7a5a48;border-radius:2px;flex:none}
.fb-page strong{color:#3b5998;font-size:7.5px}
.btn{display:inline-block;background:#4a66a4;color:#fff;font-size:7px;font-weight:700;padding:1px 4px;border-radius:2px}
.post{margin:8px 6px 0;border:1px solid #ddd;height:160px;padding:6px;font-size:7.3px;line-height:10.6px;color:#222;overflow:hidden}
.post .who{display:flex;gap:6px;margin-bottom:8px}
.post .who strong{color:#3b5998;display:block}
.post .who span{color:#888;font-size:6.5px}
.post p{margin-bottom:3px}
.tweets{padding:5px;font-size:7px;line-height:9.4px;color:#222}
.tweets .bar{display:flex;justify-content:space-between;font-weight:700;font-size:8px;border-bottom:1px solid #eee;padding-bottom:4px}
.tweets .follow{border:1px solid #ccc;border-radius:2px;font-size:6.5px;padding:0 4px;background:#f5f5f5}
.tweets .link{color:#2a6bb8;margin:3px 0 10px 2px}
.tweet{display:flex;gap:5px}
.tweet .avatar{width:16px;height:16px}
.tweet .blue{color:#2a6bb8}
.tweet-photo{margin:6px 0 0 0;width:151px;height:38px;background:linear-gradient(#4f7a2a,#8fb04c)}
.tweet-box{position:absolute;left:4px;bottom:14px;width:162px;height:18px;border:1px solid #ccc;font-size:7.5px;padding:3px 5px;color:#555}
.follow-us{left:529px;top:912px;color:#fff}
.follow-us h3{font-size:14px;font-weight:400;margin-bottom:6px}
.pill{display:block;width:max-content;font-size:7px;font-weight:700;padding:2px 4px;margin-bottom:4px;border-radius:2px;background:#eef2f8;color:#2a4a8a}
.pill.like{background:#4a66a4;color:#fff}
.pill.plus{background:#fff;color:#333;padding:2px 16px 2px 22px}
.follow-us ul{list-style:none;margin-top:12px;font-size:8.8px}
.follow-us li{margin-bottom:8.7px}
</style>
</head>
<body>

<header>
  <div class="abs site-name">The Animal Cover Handbook 2015</div>
  <div class="abs social-top"><span>Chirper</span><span>Pawbook</span><span>Linkwork</span></div>
  <div class="abs search">Search here
    <svg width="12" height="12" viewBox="0 0 12 12"><circle cx="5" cy="5" r="3.8" fill="none" stroke="#444" stroke-width="1.5"/><line x1="7.8" y1="7.8" x2="11" y2="11" stroke="#444" stroke-width="1.6"/></svg>
  </div>
</header>

<nav class="abs main-nav">
  <ul>
    <li>Home</li><li>Pet Insurnace Reviews</li><li>Providers A-Z</li><li>Pet Insurnace Policies</li><li>Surveys</li><li>More</li>
  </ul>
</nav>

<section class="feature-tiles">
  <div class="abs tile blue" style="left:131px">
    <div class="icon"><div role="img" aria-label="White dog with heart illustration" style="width:68px;height:58px;background:rgba(255,255,255,.85);border-radius:30px 30px 8px 8px"></div></div>
    <h3>Pet Insurance<br>Provider</h3>
    <p>Lorem ipsum dolor sit amet consectetuer adipis</p>
  </div>
  <div class="abs tile blue dark" style="left:317px">
    <div class="icon"><svg width="56" height="50" viewBox="0 0 56 50" fill="#fff"><ellipse cx="10" cy="22" rx="6" ry="8"/><ellipse cx="20" cy="9" rx="6" ry="8"/><ellipse cx="36" cy="9" rx="6" ry="8"/><ellipse cx="46" cy="22" rx="6" ry="8"/><path d="M28 24c-9 0-15 12-15 18 0 6 7 6 15 3 8 3 15 3 15-3 0-6-6-18-15-18z"/></svg></div>
    <h3>Pet Insurance<br>Reviews</h3>
    <p>Lorem ipsum dolor sit amet consectetuer adipis cing</p>
  </div>
  <div class="abs tile orange" style="left:502px">
    <div class="icon"><svg width="38" height="38" viewBox="0 0 38 38"><circle cx="19" cy="19" r="18" fill="#fff"/><path d="M10 19l6 6 12-13" fill="none" stroke="var(--orange)" stroke-width="5" stroke-linecap="round" stroke-linejoin="round"/></svg></div>
    <h3>Top Policies</h3>
    <p>Lorem ipsum dolor sit amet consectetuer adipis cing elit Nam cursus Morbi Nullam</p>
  </div>
  <div class="abs tile orange" style="left:688px">
    <div class="icon"><svg width="40" height="40" viewBox="0 0 40 40"><circle cx="16" cy="16" r="11" fill="none" stroke="#fff" stroke-width="6"/><line x1="24" y1="24" x2="35" y2="35" stroke="#fff" stroke-width="7" stroke-linecap="round"/></svg></div>
    <h3>Search Policy</h3>
    <p>Lorem ipsum dolor sit amet consectetuer adipis cing elit Nam cursus Morbi Nullam</p>
  </div>
</section>

<section class="content-groups">
  <div class="abs group" style="left:131px;width:236px">
    <div class="group-head"><div class="kicker">Learn</div><h2>About Pet Insurance</h2></div>
    <ul class="learn-list">
      <li>Introduction to Pet Insurance</li>
      <li>Vet Fees Cover Types</li>
      <li>What to Consider before Buying</li>
      <li>Ten Popular Pet Insurance Providers</li>
      <li>Confused by Pet Insurance: Start Here!</li>
      <li>Third Party Liability Insurance</li>
      <li>Six Vet Fees Pet Insurance Companies Won't Pay!</li>
      <li>Why Cheap Pet Insurance is Risky</li>
      <li>Why Your Pets Vet History is Important</li>
    </ul>
  </div>
  <div class="abs group" style="left:371px;width:240px">
    <div class="group-head" style="padding-left:24px"><div class="kicker">Research</div><h2 class="orange">UK Pet Insurance</h2></div>
    <div class="research-body">
      <h4>Analysis, Customer Reviews</h4>
      <div class="research-cols">
        <ul><li>Critter Cover</li><li>Brightmart</li><li>Straight Cover</li><li>F&amp;M</li><li>Happy Paws</li><li>Carewell</li><li>James Lowe</li><li>QV=</li></ul>
        <ul><li>Hound Society</li><li>P&amp;T</li><li>Beyond Cover</li><li>PetShield</li><li>Sandford's</li><li>Teskin</li><li>Vista Money</li></ul>
      </div>
      <p>Search our database for policies matching your criteria</p>
      <p>Compare claims experiences&nbsp; for pet insurance providers</p>
    </div>
  </div>
  <div class="abs group" style="left:614px;width:240px">
    <div class="group-head" style="padding-left:22px"><div class="kicker">Campaign</div><h2>For Fairer Pet Insurance</h2></div>
    <ul class="campaign-list">
      <li>This section will contain paragraphs of text</li>
      <li>Brief explanation of why a campaign is needed.</li>
      <li>Brief explanation of what to campaign for.</li>
      <li>Bio pic of me... plus brief bio.</li>
      <li>How you can help</li>
      <li>Stories with Pet Pics.</li>
    </ul>
  </div>
</section>

<section class="articles">
  <h2 class="abs section-title">Popular Articles and Resources</h2>
  <div class="abs photo" role="img" aria-label="Photo of a small dog running on grass" style="left:136px;top:716px;width:97px;height:86px;background:linear-gradient(#9cc6e8 0%,#b9d5a0 45%,#5f8f2a 100%)"></div>
  <div class="abs article" style="left:242px;top:715px">
    <h3>Pet Insurance for Pre-Existing Conditions</h3>
    <p>Aascetur ridiculus mus In iaculis facilisis massa Etiam eu urna Sed porta Suspendisse quam leo molestie sed luctus quis feugiat in pede Fusce tellus Sed metus</p>
    <span class="more">Read More</span>
  </div>
  <div class="abs photo" role="img" aria-label="Photo of a cat and a puppy sleeping together" style="left:436px;top:714px;width:98px;height:87px;background:linear-gradient(135deg,#3a2a1e,#9a6a42 55%,#5a3a24)"></div>
  <div class="abs article" style="left:542px;top:713px">
    <h3>Pet Insurance for Pre-Existing Conditions</h3>
    <p>Aascetur ridiculus mus In iaculis facilisis massa Etiam eu urna Sed porta Suspendisse quam leo molestie sed luctus quis feugiat in pede Fusce tellus Sed metus</p>
    <span class="more">Read More</span>
  </div>
  <div class="abs" role="img" aria-label="Advertisement banner for hosting packages" style="left:734px;top:689px;width:125px;height:125px;background:linear-gradient(#1e6fb0,#0e2f5e)"></div>
</section>

<footer>
  <div class="abs footer"></div>

  <div class="abs widget fb" style="left:131px">
    <div class="widget-head">Join Us on Pawbook</div>
    <div class="fb-page">
      <div class="avatar" role="img" aria-label="Page profile picture"></div>
      <div><strong>Animal Cover Reviews UK</strong><br><span class="btn">Like</span> 1,176</div>
    </div>
    <div class="post">
      <div class="who"><div class="avatar" role="img" aria-label="Page profile picture" style="width:22px;height:22px"></div>
        <div><strong>Animal Cover Reviews UK</strong><span>January 19 at 1:13pm</span></div></div>
      <p>Pet Insurance Premium Increases</p>
      <p>Interesting article from Consumer Choice suggesting that that pet insurance premiums can double as your pet ages...</p>
      <p>Have to confess that this sounds on the low side to me! Would be really</p>
    </div>
  </div>

  <div class="abs widget tw" style="left:326px">
    <div class="widget-head">Latest from Chirper</div>
    <div class="tweets">
      <div class="bar"><span>Tweets</span><span class="follow">Follow</span></div>
      <div class="link">petfinders.example/blog.php?d...</div>
      <div class="tweet">
        <div class="avatar" role="img" aria-label="Account profile picture"></div>
        <div><strong>Animal Cover Reviews</strong> &nbsp;&nbsp;&nbsp;&nbsp;&nbsp;16 Jun<br><span style="color:#888">@AnimalCoverUK</span><br>
          RT <span class="blue">@listeningpaws</span>: Not into football? We have 14 adorable hearing dog puppies who will change your mind <span class="blue">#MatchDay</span><br><span class="blue">pic.link/a8Kx21</span>
          <div class="tweet-photo" role="img" aria-label="Photo of a puppy on grass"></div>
        </div>
      </div>
    </div>
    <div class="tweet-box">Tweet to @AnimalCoverUK</div>
  </div>

  <div class="abs follow-us">
    <h3>Follow Us</h3>
    <span class="pill">Follow @AnimalCoverUK</span>
    <span class="pill like">Like</span>
    <span class="pill plus">Follow</span>
    <ul>
      <li>About Us</li>
      <li>Legal Information &amp; Disclaimers</li>
      <li>Privacy Policy</li>
    </ul>
  </div>

  <div class="abs footer-bottom">Copyright © 2015. Animal Cover Reviews UK. All Right Reserved.</div>
</footer>

</body>
</html>
```